Kings of Polished Fog*

I am looking for a book cover which will really pop. Working title: Kings of Polished Fog (or K.P.F. for short) The concept behind the book is: education is too expensive, screwed up, and basically failing us, and even an MBA is not worth it's name anymore! How a BS is Brilliantly Stupid, a BA is great to be a Broke Artist, an MA is Mostly Antiquated and a MS Mastered Something? ...you get the point, basically I'll be ripping into a whole bunch of degree types, then walking you through what you should actually learn from an MBA. It is going to be written with a fair bit of humor, while still being fact driven. Target audience is working professionals who are considering an MBA, or have one and want a $15 refresher of all they spent $90k+ on. No color scheme is requested, Since i do like to allow creativity to flow!

Book size 5" by 8" and ebook. Author is: R.J. Halvorsen size format attached.

Went on vacation/holiday

• K.P.F. (but can be an emphasises in the Kings of Polished Fog title.
• If you look at "Lanterns over Elm Creek: a gentle account of harvest seasons on the northern farm" on brindlecart, you can see a blue/silver/white color scheme I liked in the past - but dont take that as a must by any means, the second choice was a completely different (red and white) scheme

```html
<!DOCTYPE html>
<html lang="en">
<head>
<meta charset="utf-8">
<title>Kings of Polished Fog – Cover</title>
<link rel="stylesheet" href="https://fonts.googleapis.com/css2?family=Cinzel:wght@400;500&family=Crimson+Text&family=UnifrakturMaguntia&display=swap">
<style>
  :root {
    --stage: #2b2b2e;
    --wrap-light: #ecebe7;
    --wrap-mid: #bdb9b2;
    --wrap-dark: #8c877f;
    --ink: #1c1b1a;
    --body-ink: #2a2826;
    --gold: #b08a3a;
    --gold-light: #d9b866;
    --gold-dark: #7e5f22;
    --holder-dark: #5a5854;
    --holder-mid: #8f8c87;
    --paper: #f3f2ef;
    --paper-shade: #d6d4cf;
  }
  * { box-sizing: border-box; margin: 0; padding: 0; }
  html, body { width: 828px; height: 1200px; overflow: hidden; background: var(--stage); }
  .canvas { position: relative; width: 828px; height: 1200px; }

  .full-wrap {
    position: absolute; left: 18px; top: 35px; width: 792px; height: 552px;
    background: radial-gradient(ellipse 90% 80% at 45% 15%, var(--wrap-light) 0%, var(--wrap-mid) 60%, var(--wrap-dark) 100%);
    overflow: hidden;
  }
  .back-title {
    position: absolute; left: 0; width: 380px; top: 38px; text-align: center;
    font-family: "UnifrakturMaguntia", serif; font-size: 44px; color: var(--ink);
  }
  .back-blurb {
    position: absolute; left: 17px; top: 100px; width: 352px;
    font-family: "Crimson Text", serif; font-size: 11.2px; line-height: 14.6px;
    color: var(--body-ink); text-align: justify;
  }
  .back-blurb p + p { margin-top: 14px; }

  .spine {
    position: absolute; left: 380px; top: 0; width: 32px; height: 552px;
  }
  .spine-text {
    position: absolute; left: 28px; top: 20px; width: 522px; height: 30px;
    transform: rotate(90deg); transform-origin: 0 0;
    display: flex; align-items: center; gap: 14px; white-space: nowrap;
  }
  .spine-title { font-family: "UnifrakturMaguntia", serif; font-size: 22px; color: var(--gold); }
  .spine-subtitle { font-family: "Cinzel", serif; font-size: 11px; line-height: 12px; color: var(--ink); }
  .spine-author { margin-left: auto; font-family: "Cinzel", serif; font-size: 15px; color: var(--ink); }

  .front-cover {
    position: absolute; width: 380px; height: 552px; overflow: hidden;
    transform-origin: 0 0;
  }
  .front-cover--wrap { left: 412px; top: 0; }
  .front-cover--single { left: 473px; top: 642px; transform: scale(0.876, 0.902); }
  .cover-photo {
    position: absolute; inset: 0;
    background: linear-gradient(90deg, var(--holder-dark) 0%, var(--holder-mid) 10%, var(--paper-shade) 22%, var(--paper) 32%, var(--paper) 78%, var(--paper-shade) 86%, var(--holder-mid) 94%, var(--holder-dark) 100%);
  }
  .cover-content {
    position: absolute; left: 90px; width: 230px; top: 0; height: 100%; text-align: center;
  }
  .cover-title {
    position: absolute; left: -20px; right: -20px; top: 88px;
    font-family: "UnifrakturMaguntia", serif; font-size: 56px; line-height: 1;
    color: var(--gold);
    background: linear-gradient(180deg, var(--gold-light), var(--gold) 55%, var(--gold-dark));
    -webkit-background-clip: text; background-clip: text; -webkit-text-fill-color: transparent;
  }
  .cover-subtitle {
    position: absolute; left: -20px; right: -20px; top: 210px;
    font-family: "Cinzel", serif; font-size: 18px; line-height: 25px; color: var(--ink);
  }
  .cover-decree {
    position: absolute; left: 0; right: 0; top: 278px;
    font-family: "Crimson Text", serif; font-size: 10px; line-height: 12px; color: var(--body-ink);
  }
  .signature-row {
    position: absolute; left: 0; right: 0; top: 360px; height: 40px;
  }
  .signature-line { position: absolute; height: 1px; width: 50px; background: var(--body-ink); }
  .seal {
    position: absolute; left: 100px; top: 2px; width: 30px; height: 30px; border-radius: 50%;
    background: radial-gradient(circle at 40% 35%, var(--gold-light), var(--gold) 55%, var(--gold-dark));
  }
  .cover-author {
    position: absolute; left: -30px; right: -30px; top: 446px;
    font-family: "Cinzel", serif; font-size: 33px; line-height: 45px; color: var(--ink);
  }
</style>
</head>
<body>
<main class="canvas">
  <section class="full-wrap">
    <div class="back-cover">
      <h2 class="back-title">K.P.F.</h2>
      <div class="back-blurb">
        <p>Lorem ipsum dolor sit amet, consectetur adipiscing elit. Pellentesque augue ante, venenatis eu pellentesque quis, lacinia eu augue. Interdum et malesuada fames ac ante ipsum primis in faucibus. Etiam ullamcorper velit id ex viverra, et pharetra erat bibendum. Nulla vel libero iaculis, accumsan lacus non, viverra leo. Pellentesque mollis diam eu turpis rutrum, quis vestibulum sapien finibus. Phasellus commodo orci eget metus bibendum posuere.</p>
        <p>Suspendisse eros enim, varius mattis varius at, tincidunt vitae augue. Ut non facilisis arcu. Curabitur rutrum mi in sem suscipit egestas. Sed tempor libero in ligula tincidunt blandit. Suspendisse fringilla pharetra dolor vel iaculis. Sed cursus vulputate ipsum, at venenatis mauris tristique sed.</p>
        <p>Nunc ac urna tristique, congue dolor et, semper diam. Etiam pulvinar diam nec mollis pulvinar. Ut et augue vitae nunc ultrices tempor. Suspendisse vestibulum sem augue, tincidunt sodales lectus vestibulum vitae. Donec scelerisque eu nisl ut tempor. Nunc molestie commodo nibh, eu placerat justo.</p>
      </div>
    </div>

    <div class="spine">
      <div class="spine-text">
        <span class="spine-title">K.P.F.</span>
        <span class="spine-subtitle">Kings of<br>Polished Fog</span>
        <span class="spine-author">Author Name</span>
      </div>
    </div>

    <article class="front-cover front-cover--wrap">
      <div class="cover-photo" role="img" aria-label="Photograph of a toilet paper roll on a grey wall holder, the sheet hanging down like a diploma"></div>
      <div class="cover-content">
        <h1 class="cover-title">K.P.F.</h1>
        <p class="cover-subtitle">Kings of<br>Polished Fog</p>
        <p class="cover-decree">with all the honors, rights, privileges thereunto appertaining in testimony whereof, we have affixed our signatures with the seal of the university</p>
        <div class="signature-row">
          <span class="signature-line" style="left:30px;top:24px"></span>
          <span class="seal"></span>
          <span class="signature-line" style="left:150px;top:14px"></span>
          <span class="signature-line" style="left:150px;top:30px"></span>
        </div>
        <p class="cover-author">Author<br>Name</p>
      </div>
    </article>
  </section>

  <article class="front-cover front-cover--single">
    <div class="cover-photo" role="img" aria-label="Photograph of a toilet paper roll on a grey wall holder, the sheet hanging down like a diploma"></div>
    <div class="cover-content">
      <h1 class="cover-title">K.P.F.</h1>
      <p class="cover-subtitle">Kings of<br>Polished Fog</p>
      <p class="cover-decree">with all the honors, rights, privileges thereunto appertaining in testimony whereof, we have affixed our signatures with the seal of the university</p>
      <div class="signature-row">
        <span class="signature-line" style="left:30px;top:24px"></span>
        <span class="seal"></span>
        <span class="signature-line" style="left:150px;top:14px"></span>
        <span class="signature-line" style="left:150px;top:30px"></span>
      </div>
      <p class="cover-author">Author<br>Name</p>
    </div>
  </article>
</main>
</body>
</html>
```